Carwash Signage

We own and operate a 25m tunnel car wash in the uk. We are looking to upgrade our signage to include the following:-

Wash selection Board Size-1300x1300mm
Conditions 1300x1300mm
Instructions 1300x1300mm
Banner 2600x600mm
Stamp card flyer a5 double sided - 9 squares for stamping 3rd square needs to say free air freshener 9th square needs to say free vip car wash.

I have attached some notes for the details that are required to be included.

We are looking for a modern smart look more European car wash style than American car wash style. It should be bold and clear. with yellow/orange & blue/green,grey colours

The final design must be in a industry standard printable format.

UPDATED BRIEF AS DISCUSSED: We require design for 2 x window decals, flag design and 50% off voucher. Attached are rough layout drawings of what they should look like - we expect the designs to be in keeping with the previous designs colours, etc that have been carried out. We Look forward to hearing from you.

Target Market(s)

local car owners within a 15-20 mile radius

Colors
0054AA
0677BA
7BADD7
CADEEF
E8F1F8
0094D4
00A9DD
6FCCEA
C7EBF8
E9F6FB
00AB8E
00BBA5
67D7C9
C6EFE9
E9F9F6

Requirements
Must have
• must be sharp and modern European look

```html
<!DOCTYPE html>
<html lang="en">
<head>
<meta charset="utf-8">
<title>Riviera Car Wash – Signage Set</title>
<link href="https://fonts.googleapis.com/css2?family=Barlow+Condensed:wght@400;500;600;700;800&family=PT+Sans&family=Kaushan+Script&family=Permanent+Marker&display=swap" rel="stylesheet">
<style>
:root{
  --stage:#0c1a2e;
  --caption:#b9bec8;
  --blue:#3c68b6;
  --blue-deep:#2f5aa8;
  --sky:#58b5f6;
  --ink:#1f2d55;
  --dark:#3a3a3c;
  --vip:#e3e3e3;
  --gold:#f6d486;
  --silver:#e8e8e8;
  --bronze:#f8a979;
  --white:#ffffff;
  --cond:"Barlow Condensed",sans-serif;
}
*{box-sizing:border-box;margin:0;padding:0}
html,body{width:1200px;height:734px;overflow:hidden;background:var(--stage)}
.sheet{position:relative;width:1200px;height:734px;font-family:var(--cond)}
.caption{position:absolute;font-family:"PT Sans",sans-serif;font-size:19.5px;color:var(--caption);transform:translateX(-50%);white-space:nowrap;line-height:1}
.sign{position:absolute;background:var(--white);overflow:hidden}

/* price board */
.board{left:54px;top:110px;width:312px;height:312px;display:grid;
  grid-template-columns:41fr 31fr 24fr 22fr 28fr 28fr 21fr 21fr 26fr 17fr 23fr 29fr;
  grid-template-rows:59fr 50fr 50fr 50fr 50fr 51fr;background:#c9c9c9;gap:1px}
.board .head{background:var(--blue);color:var(--white);font-size:4.6px;font-weight:600;line-height:1.15;text-align:center;display:flex;align-items:center;justify-content:center;border-radius:0 0 2px 2px}
.board .head.roof{flex-direction:column;gap:2px;font-size:4.4px}
.board .head.roof b{font-size:5.5px;font-weight:600}
.board .options{background:var(--white);display:flex;flex-direction:column;align-items:center;padding-top:5px}
.board .brand-mini{font-size:5.5px;font-weight:700;color:var(--blue);letter-spacing:.3px}
.board .options h3{font-size:10px;font-weight:800;color:var(--blue);margin-top:1px}
.board .options .art{width:32px;height:22px;margin-top:3px;background:linear-gradient(#7bb5f5,#3c68b6);border-radius:2px}
.board .price-head{background:var(--dark);color:var(--white);font-size:10px;font-weight:700;display:flex;align-items:center;justify-content:center;border-radius:0 0 3px 3px}
.board .tier{display:flex;align-items:center;justify-content:center}
.medal{width:37px;height:37px;border-radius:50%;display:flex;align-items:center;justify-content:center;font-size:8.5px;font-weight:800;text-align:center;line-height:.95}
.cell{display:flex;align-items:center;justify-content:center;font-size:15px;font-weight:700;color:#6a6a6a}
.price{background:var(--dark);color:var(--white);font-size:9.5px;font-weight:500;display:flex;align-items:center;justify-content:center;border-radius:3px}
.r-vip{background:var(--vip)}
.r-gold{background:var(--gold)}.r-gold.cell{color:#8a4a06}
.r-silver{background:var(--silver)}
.r-bronze{background:var(--bronze)}.r-bronze.cell{color:#7a3210}
.m-vip{background:radial-gradient(circle at 40% 35%,#fff,#b9b9b9);color:#7a7a7a;font-size:7.5px}
.m-gold{background:radial-gradient(circle at 40% 35%,#fbe59a,#c8922c);color:#5a3a05}
.m-silver{background:radial-gradient(circle at 40% 35%,#fff,#b5b5b5);color:#6b6b6b}
.m-bronze{background:radial-gradient(circle at 40% 35%,#e9a574,#9c5a32);color:#4c2410}
.price.p-gold{color:var(--gold)}.price.p-bronze{color:var(--bronze)}
.offers-label{background:var(--dark);color:var(--white);font-size:11.5px;font-weight:700;display:flex;align-items:center;justify-content:center}
.offers{grid-column:2/13;background:var(--blue);color:var(--white);display:flex;justify-content:space-around;align-items:center;text-align:center;line-height:1.1}
.offers .marker{font-family:"Permanent Marker",cursive;font-size:9.5px}
.offers .big{font-size:13px;font-weight:700}
.offers .small{font-size:9.5px;font-weight:500}

/* instructions */
.instructions{left:447px;top:110px;width:312px;height:312px}
.wave{position:absolute;left:0;top:0}
.instructions h2{position:absolute;left:0;width:100%;top:23px;text-align:center;font-size:38px;font-weight:800;color:var(--blue);letter-spacing:.5px;line-height:1}
.step{position:absolute;left:13px;font-size:10.6px;color:var(--ink);line-height:1.25;white-space:nowrap}
.step::before{content:"★";position:absolute;left:0;top:0}
.step span{display:block;padding-left:12px}
.sub{position:absolute;font-size:8px;color:var(--ink);white-space:nowrap}
.sub i{font-style:normal;margin-right:6px}
.sub i::before{content:"● ";font-size:6px}
.wash-art{position:absolute;background:linear-gradient(180deg,#9bcaf8,#3c78d2);border-radius:3px}
.footer-band{position:absolute;left:0;bottom:0;width:100%;height:22px;background:var(--sky);display:flex;align-items:center;justify-content:center;font-family:"Kaushan Script",cursive;color:var(--white);font-size:11px}

/* conditions */
.conditions{left:839px;top:110px;width:312px;height:312px}
.brand{position:absolute;color:var(--ink);font-weight:700;line-height:1}
.brand small{display:block;font-size:8.5px;letter-spacing:2px;text-align:right}
.brand strong{display:block;font-size:26px;letter-spacing:1px;font-weight:700}
.conditions .lead{position:absolute;left:22px;top:70px;width:275px;font-size:10.4px;color:var(--ink);line-height:1.35}
.conditions .lead b{font-weight:700}
.reasons{position:absolute;list-style:none;font-size:9.6px;color:var(--ink);line-height:13px}
.reasons li::before{content:"★ ";font-size:8px}
.conditions .note{position:absolute;left:12px;top:167px;width:288px;text-align:center;font-size:9.4px;color:var(--ink);line-height:1.33}

/* banner */
.banner{left:291px;top:505px;width:624px;height:144px}
.banner .attended{position:absolute;left:12px;top:9px;font-size:21px;font-weight:800;color:var(--white);line-height:1}
.banner .headline{position:absolute;left:103px;top:30px;font-size:93px;font-weight:800;color:var(--blue);line-height:1;letter-spacing:1px}
.banner .pay-band{position:absolute;left:0;top:113px;width:100%;height:31px;background:var(--sky)}
.banner .pay{position:absolute;left:18px;top:117px;font-size:19px;font-weight:600;color:var(--white);line-height:1}
.banner .card{position:absolute;left:264px;top:116px}
.banner .clock-art{position:absolute;left:489px;top:55px;width:93px;height:53px;background:radial-gradient(circle at 45% 55%,#ffffff 0 30%,#3c68b6 31% 45%,#7fbff7 46% 70%,transparent 71%)}
.banner .open{position:absolute;right:9px;top:99px;font-size:13px;font-weight:700;color:var(--blue);line-height:1}
.banner .hours{position:absolute;right:9px;top:115px;font-size:11px;font-weight:500;color:var(--white);line-height:13px;text-align:right}
.banner .hours span{display:inline-block;width:30px;text-align:left}
</style>
</head>
<body>
<main class="sheet">
  <p class="caption" style="left:209px;top:80px">Board Size-1300x1300mm</p>
  <p class="caption" style="left:603px;top:80px">Instructions 1300x1300mm</p>
  <p class="caption" style="left:995px;top:80px">Conditions 1300x1300mm</p>
  <p class="caption" style="left:602px;top:468px">Banner 2600x600mm</p>

  <!-- price board -->
  <section class="sign board" aria-label="Wash selection price board">
    <div class="options">
      <span class="brand-mini">RIVIERA</span>
      <h3>OPTIONS</h3>
      <div class="art" role="img" aria-label="Car wash tunnel illustration"></div>
    </div>
    <div class="head roof"><b>ROOF<br>BRUSH</b><span>6 CONTOUR<br>BRUSHES</span><span>SILL<br>BRUSHES</span></div>
    <div class="head">DRYING<br>DOUBLE<br>CONTOUR</div>
    <div class="head">WAXING</div>
    <div class="head">HAND<br>BRUSH<br>PREPARED</div>
    <div class="head">ACTIVE<br>FOAM<br>PRE SOAK</div>
    <div class="head">ALLOY<br>WHEEL<br>SPRAY</div>
    <div class="head">JADE<br>ULTRA<br>WAX</div>
    <div class="head">JET<br>WASH<br>PRE WASH</div>
    <div class="head">UNDER<br>BODY<br>WASH</div>
    <div class="head">SNOW<br>FOAM<br>PREWASH</div>
    <div class="price-head">PRICE</div>

    <div class="tier r-vip"><div class="medal m-vip">VIP<br>PLATINUM</div></div>
    <div class="cell r-vip">✱</div><div class="cell r-vip">✱</div><div class="cell r-vip">✱</div><div class="cell r-vip">✱</div><div class="cell r-vip">✱</div><div class="cell r-vip">✱</div><div class="cell r-vip">✱</div><div class="cell r-vip">✱</div><div class="cell r-vip">✱</div><div class="cell r-vip">✱</div>
    <div class="price">£10.00</div>

    <div class="tier r-gold"><div class="medal m-gold">GOLD</div></div>
    <div class="cell r-gold">✱</div><div class="cell r-gold">✱</div><div class="cell r-gold">✱</div><div class="cell r-gold">✱</div><div class="cell r-gold">✱</div><div class="cell r-gold">✱</div><div class="cell r-gold">✱</div><div class="cell r-gold">✱</div><div class="cell r-gold"></div><div class="cell r-gold"></div>
    <div class="price p-gold">£8.50</div>

    <div class="tier r-silver"><div class="medal m-silver">SILVER</div></div>
    <div class="cell r-silver">✱</div><div class="cell r-silver">✱</div><div class="cell r-silver">✱</div><div class="cell r-silver">✱</div><div class="cell r-silver">✱</div><div class="cell r-silver"></div><div class="cell r-silver"></div><div class="cell r-silver"></div><div class="cell r-silver"></div><div class="cell r-silver"></div>
    <div class="price">£7.50</div>

    <div class="tier r-bronze"><div class="medal m-bronze">BRONZE</div></div>
    <div class="cell r-bronze">✱</div><div class="cell r-bronze">✱</div><div class="cell r-bronze">✱</div><div class="cell r-bronze">✱</div><div class="cell r-bronze"></div><div class="cell r-bronze"></div><div class="cell r-bronze"></div><div class="cell r-bronze"></div><div class="cell r-bronze"></div><div class="cell r-bronze"></div>
    <div class="price p-bronze">£6.50</div>

    <div class="offers-label">OFFERS</div>
    <div class="offers">
      <div><div class="marker">VIP PLATINUM WASH PACK</div><div class="big">BUY 2 GET 1 FREE</div><div class="small">£20.00</div></div>
      <div><div class="marker">LOYALTY CARD AVAILABLE</div><div class="big">WASH + EARN</div><div class="small">ASK THE OPERATOR FOR DETAILS</div></div>
    </div>
  </section>

  <!-- instructions -->
  <section class="sign instructions" aria-label="Instructions board">
    <svg class="wave" width="312" height="312" viewBox="0 0 312 312"><path d="M0 0H312V37C292 26 262 6 212 4C150 2 90 20 0 22Z" fill="var(--blue)"/></svg>
    <h2>INSTRUCTIONS</h2>
    <p class="step" style="top:66px"><span>Check for loose items before entering the wash</span></p>
    <p class="step" style="top:83px"><span>Lower aerial if electrical make sure the aerial is fully retracted</span><span>Operator may assist but is not responsible for the condition of your car.</span></p>
    <p class="step" style="top:112px"><span>Lower aerial if electrical make sure the aerial is fully retracted</span><span>Drive forward untill operator tells you to stop</span></p>
    <p class="step" style="top:142px"><span>Operator will guide you into the carwash</span></p>
    <p class="step" style="top:160px"><span>Once on conveyor track:</span></p>
    <p class="sub" style="left:29px;top:177px"><i>Hand brake off</i><i>Select neutral gear</i><i>Close all windows and sunroof</i></p>
    <p class="sub" style="left:45px;top:191px"><i>Leave engine running</i><i>Turn auto wipers off</i></p>
    <p class="step" style="top:207px"><span>Do not brake</span></p>
    <p class="step" style="top:223px"><span>Do not steer</span></p>
    <p class="step" style="top:239px"><span>Do not attempt exit vehicle</span></p>
    <p class="step" style="top:255px"><span>At the end of wash drive away</span><span>when trafficLight turns green</span></p>
    <div class="wash-art" role="img" aria-label="Car passing through a brush wash tunnel" style="left:170px;top:217px;width:90px;height:66px"></div>
    <div class="footer-band">Enjoy The Ride</div>
  </section>

  <!-- conditions -->
  <section class="sign conditions" aria-label="Conditions board">
    <svg class="wave" width="312" height="312" viewBox="0 0 312 312"><path d="M0 0H312V37C292 26 262 6 212 4C150 2 90 20 0 22Z" fill="var(--blue)"/></svg>
    <div class="brand" style="left:60px;top:18px"><small>CAR WASH</small><strong>● RIVIERA</strong></div>
    <p class="lead"><b>RIVIERA CARS + COMMERCIAL LTD</b> cannot accept any responsibility for injury loss or damage caused by the following:</p>
    <ul class="reasons" style="left:46px;top:106px"><li>damaged bodywork</li><li>loose exhaust trims</li><li>Painted wheels</li><li>loose wing mirrors</li></ul>
    <ul class="reasons" style="left:143px;top:106px"><li>non fully retractable aerials</li><li>roof races</li><li>loose trims</li></ul>
    <p class="note">Remember the operator is here to help - if in doubt please ask for advice before entering the wash claims for damage cannot be entering once vehicle has left site.</p>
    <div class="wash-art" role="img" aria-label="Car passing through a brush wash tunnel" style="left:108px;top:223px;width:100px;height:78px"></div>
  </section>

  <!-- banner -->
  <section class="sign banner" aria-label="Attended car wash banner">
    <svg class="wave" width="624" height="144" viewBox="0 0 624 144"><rect width="624" height="144" fill="var(--blue)"/><path d="M0 45C100 40 200 5 330 6C460 8 520 20 560 40C600 58 615 70 624 78V113H0Z" fill="var(--white)"/></svg>
    <p class="attended">ATTENDED</p>
    <p class="headline">CAR WASH</p>
    <div class="brand" style="right:9px;top:7px;color:var(--white)"><small>CAR WASH</small><strong style="font-size:23px">● RIVIERA</strong></div>
    <div class="clock-art" role="img" aria-label="Stopwatch and gears illustration"></div>
    <p class="open">OPEN TIMING</p>
    <div class="pay-band"></div>
    <p class="pay">CASH + CARD PAYMENTS ACCEPTED</p>
    <svg class="card" width="40" height="24" viewBox="0 0 40 24" aria-hidden="true"><rect width="40" height="24" rx="2" fill="var(--white)"/><rect x="3" y="7" width="34" height="3" fill="var(--blue)"/><rect x="3" y="14" width="12" height="2" fill="var(--blue)"/><rect x="3" y="18" width="9" height="2" fill="var(--blue)"/><circle cx="25" cy="18" r="2.5" fill="var(--blue)"/><circle cx="29" cy="18" r="2.5" fill="var(--blue)"/><circle cx="33" cy="18" r="2.5" fill="var(--blue)"/></svg>
    <p class="hours"><span>MON-SAT</span> – 8:00 - 18:00<br><span>SUN</span> – 9:00 - 18:00</p>
  </section>
</main>
</body>
</html>
```